Business Cards Needed For Veterinary Business

Looking for a business card design for a veterinary blood bank. We would like it to be clean and professional on appearance but still warm and inviting. We would like to utilize our logo and similar coloring. We will use our phone number, email, website, employee name, employee title.

We do not want a bunch of animated animal photos but do not need the style to be as clinical as a laboratory or human medical procedure office.

We are looking for some creative ideas to choose from so that we can generate a standout professional business card for our management team to utilize.

Target Market(s)

professionals

Industry/Entity Type

veterinary

Contact Information for Business Card

employee name, employee title, phone number, website URL, email

Font styles to use
Sans Serif

Colors
0054AA
0677BA
7BADD7
CADEEF
E8F1F8
EB3D1F
EC4F4E
F09395
F8D3D4
FCEDEE

Requirements
Nice to have
• creative design
Should not have
• animated photos

```html
<!DOCTYPE html>
<html lang="en">
<head>
<meta charset="utf-8">
<title>Larkfield Pet Blood Bank – Business Cards</title>
<link href="https://fonts.googleapis.com/css2?family=Montserrat:wght@500;600;700;800&display=swap" rel="stylesheet">
<style>
  :root {
    --stage: #4a4a4c;
    --card-white: #f4f4f3;
    --brand-blue: #0054AA;
    --brand-blue-deep: #0b4c96;
    --brand-red: #EB3D1F;
    --edge-red: #c8161d;
    --ink-grey: #5e5e60;
    --rule-grey: #9a9a9a;
    --on-blue: #f2f4f7;
  }
  * { box-sizing: border-box; margin: 0; padding: 0; }
  html, body { width: 1200px; height: 1108px; overflow: hidden; }
  body {
    background: var(--stage);
    font-family: "Montserrat", sans-serif;
    position: relative;
  }
  .card {
    position: absolute;
    width: 640px;
    height: 366px;
    border-bottom: 5px solid var(--edge-red);
    box-shadow: 0 18px 40px rgba(0,0,0,0.35);
  }
  .card--front { left: 280px; top: 130px; background: var(--card-white); }
  .card--back  { left: 280px; top: 600px; background: var(--brand-blue); }

  .brand {
    position: absolute;
    display: flex;
    align-items: center;
    gap: 14px;
    font-weight: 800;
    text-transform: uppercase;
    letter-spacing: 0.5px;
  }
  .brand__dot {
    width: 26px; height: 26px; border-radius: 50%;
    flex: none;
  }
  .brand__name { font-size: 40px; line-height: 1; }
  .brand__tagline { display:block; font-size: 17px; letter-spacing: 2px; margin-top: 8px; }

  .card--front .brand { left: 150px; top: 90px; color: var(--brand-red); }
  .card--front .brand__dot { background: var(--brand-red); }
  .card--back .brand { left: 150px; top: 105px; color: var(--on-blue); }
  .card--back .brand__dot { background: var(--on-blue); }

  .holder {
    position: absolute;
    left: 120px; top: 240px;
    width: 200px;
    text-align: right;
  }
  .holder__name { color: var(--brand-red); font-weight: 800; font-size: 21px; letter-spacing: 0.5px; }
  .holder__title { color: var(--ink-grey); font-weight: 600; font-size: 14px; margin-top: 4px; }

  .divider {
    position: absolute;
    left: 336px; top: 232px;
    width: 1.5px; height: 76px;
    background: var(--rule-grey);
  }
  .contact {
    position: absolute;
    left: 352px; top: 234px;
    list-style: none;
  }
  .contact__item {
    display: flex; align-items: center; gap: 10px;
    font-size: 14px; font-weight: 500; color: #333;
    height: 24px;
  }
  .contact__item svg { width: 13px; height: 13px; fill: var(--brand-blue); flex: none; }

  .card--back .site {
    position: absolute;
    left: 0; right: 0; bottom: 62px;
    text-align: center;
    color: var(--on-blue);
    font-weight: 600;
    font-size: 15px;
    letter-spacing: 0.5px;
  }
</style>
</head>
<body>
  <section class="card card--front">
    <div class="brand">
      <span class="brand__dot"></span>
      <span>
        <span class="brand__name">Larkfield</span>
        <span class="brand__tagline">Pet Blood Bank</span>
      </span>
    </div>
    <div class="holder">
      <p class="holder__name">DANIEL REYES</p>
      <p class="holder__title">President</p>
    </div>
    <div class="divider"></div>
    <ul class="contact">
      <li class="contact__item">
        <svg viewBox="0 0 24 24"><path d="M6.6 10.8a15.2 15.2 0 0 0 6.6 6.6l2.2-2.2a1 1 0 0 1 1-.25 11.4 11.4 0 0 0 3.6.57 1 1 0 0 1 1 1V20a1 1 0 0 1-1 1A17 17 0 0 1 3 4a1 1 0 0 1 1-1h3.5a1 1 0 0 1 1 1c0 1.25.2 2.45.57 3.57a1 1 0 0 1-.25 1z"/></svg>
        555-018-4420
      </li>
      <li class="contact__item">
        <svg viewBox="0 0 24 24"><path d="M2 5h20v14H2z M4 7v.5l8 5 8-5V7l-8 5z"/></svg>
        hello@larkfieldpbb.com
      </li>
      <li class="contact__item">
        <svg viewBox="0 0 24 24"><circle cx="12" cy="12" r="10"/></svg>
        www.larkfieldpbb.com
      </li>
    </ul>
  </section>

  <section class="card card--back">
    <div class="brand">
      <span class="brand__dot"></span>
      <span>
        <span class="brand__name">Larkfield</span>
        <span class="brand__tagline">Pet Blood Bank</span>
      </span>
    </div>
    <p class="site">www.larkfieldpbb.com</p>
  </section>
</body>
</html>
```